Product flyer with pricing

We manufacture iconic and luxury vending trailers. for our first trailer we need a flyer created to give to prospective clients with base pricing. I am uploading an example along with graphic files.

```html
<!DOCTYPE html>
<html lang="en">
<head>
<meta charset="utf-8">
<title>Classic Barnhouse Mini – Product Flyer</title>
<link href="https://fonts.googleapis.com/css2?family=Poppins:wght@300;400;500;600;700;800&display=swap" rel="stylesheet">
<style>
:root{
  --yellow:#eba714;
  --green:#3c8d2f;
  --green-text:#3f932f;
  --ink:#222;
  --grey-photo:#5d5f62;
  --grey-photo-dark:#3f4144;
  --line:#dcdcdc;
  --page:#e8e5e0;
  --white:#fff;
}
*{box-sizing:border-box;margin:0;padding:0}
html,body{width:1200px;height:960px;overflow:hidden;background:var(--page);font-family:'Poppins',sans-serif;color:var(--ink)}
.stage{position:relative;width:1200px;height:960px}
.flyer{position:absolute;left:273px;top:22px;width:816px;height:1145px;background:var(--white);transform:scale(.8);transform-origin:0 0;overflow:hidden;box-shadow:0 4px 18px rgba(0,0,0,.18)}
.top-bar{position:absolute;left:0;top:0;width:100%;height:20px;background:var(--yellow)}
.hero-photo{position:absolute;left:0;top:20px;width:100%;height:392px;background:linear-gradient(180deg,var(--grey-photo) 0%,#6b6d70 45%,var(--grey-photo-dark) 100%)}
.logo-tab{position:absolute;left:232px;top:0;width:352px;height:118px}
.brand{position:absolute;left:0;top:48px;width:816px;text-align:center;display:flex;justify-content:center;align-items:center;gap:8px}
.brand-dot{width:14px;height:14px;border-radius:50%;background:var(--green)}
.brand-name{font-weight:700;font-size:19px;color:var(--green-text);letter-spacing:.3px}
.headline{position:absolute;left:0;top:150px;width:100%;text-align:center;color:var(--white)}
.headline .the{font-weight:400;font-size:40px;line-height:1.1}
.headline .name{font-weight:800;font-size:52px;color:var(--yellow);line-height:1.15;margin-top:4px}
.headline .sub{font-weight:400;font-size:42px;line-height:1.15;letter-spacing:.3px}
.thumbs{position:absolute;top:340px;left:65px;display:flex;gap:21px}
.thumb{width:216px;height:135px;border:4px solid var(--yellow);border-radius:11px;background:linear-gradient(180deg,#9db4cf 0%,#d9dde2 45%,#f4f4f4 70%,#6f7276 100%)}
.section-title{position:absolute;left:0;width:100%;text-align:center;font-weight:600;font-size:21px}
.features-title{top:519px;color:var(--green-text)}
.features-title span{background:var(--white);padding:0 18px}
.features-box{position:absolute;left:24px;top:533px;width:769px;height:177px;border:1.5px solid var(--line);border-radius:8px}
.list{list-style:none}
.list li{position:relative;padding-left:20px;font-size:14.2px;line-height:20px;margin-bottom:5px}
.list li::before{content:"";position:absolute;left:2px;top:8px;width:5px;height:5px;border-radius:50%;background:var(--green)}
.features-left{position:absolute;left:48px;top:564px;width:350px}
.features-right{position:absolute;left:428px;top:562px;width:360px}
.divider{position:absolute;left:408px;top:566px;width:1px;height:106px;background:var(--line)}
.price-pill{position:absolute;left:292px;top:697px;width:233px;height:27px;border-radius:14px;background:var(--yellow);color:var(--white);display:flex;align-items:center;justify-content:center;gap:8px}
.price-pill .label{font-size:13px;font-weight:400}
.price-pill .amount{font-size:19px;font-weight:700}
.options-band{position:absolute;left:0;top:762px;width:100%;height:204px;background:linear-gradient(90deg,#3d8c30 0%,#4a9a3a 50%,#3d8c30 100%)}
.options-title{top:777px;color:var(--white)}
.rule{position:absolute;top:792px;height:1.5px;background:rgba(255,255,255,.8)}
.options-band .list li::before,.options-list li::before{background:var(--yellow)}
.options-list{position:absolute;list-style:none;color:var(--white)}
.options-list li{position:relative;padding-left:20px;font-size:14.2px;line-height:20px}
.options-list li::before{content:"";position:absolute;left:2px;top:8px;width:5px;height:5px;border-radius:50%}
.options-left{left:28px;top:830px}
.options-right{left:426px;top:830px}
.options-list .note{display:block;font-size:11px;font-style:italic;color:var(--yellow);line-height:15px}
.opt-divider{position:absolute;left:410px;top:834px;width:1px;height:80px;background:rgba(255,255,255,.6)}
.tag{position:absolute;height:23px;padding:0 10px 0 16px;background:var(--yellow);color:var(--white);font-weight:700;font-size:15px;display:flex;align-items:center;clip-path:polygon(8px 0,100% 0,100% 100%,8px 100%,0 50%);border-radius:2px}
.tag.sm{font-size:13.5px}
.usecases-tab{position:absolute;left:290px;top:950px;width:236px;height:40px}
.usecases-title{position:absolute;left:290px;top:955px;width:236px;text-align:center;color:var(--white);font-weight:600;font-size:21px}
.cases{position:absolute;list-style:none}
.cases li{position:relative;padding-left:20px;margin-bottom:12px}
.cases li::before{content:"";position:absolute;left:2px;top:7px;width:5px;height:5px;border-radius:50%;background:var(--yellow)}
.cases .case-name{display:block;font-weight:600;font-size:13px;color:var(--yellow);line-height:18px}
.cases .case-desc{display:block;font-size:12.5px;line-height:18px}
.cases-left{left:28px;top:1008px}
.cases-right{left:426px;top:1008px}
.bottom-bar{position:absolute;left:0;bottom:0;width:100%;height:16px;background:var(--yellow)}
</style>
</head>
<body>
<div class="stage">
  <article class="flyer">
    <div class="top-bar"></div>
    <div class="hero-photo" role="img" aria-label="Photo of the white board-and-batten vending trailer with dark roof and bare trees behind, darkened as a backdrop"></div>

    <svg class="logo-tab" viewBox="0 0 352 118" aria-hidden="true">
      <path d="M0 0 L352 0 L310 88 Q298 114 270 114 L82 114 Q54 114 42 88 Z" fill="#fff" stroke="#eba714" stroke-width="4"/>
    </svg>
    <div class="brand"><span class="brand-dot"></span><span class="brand-name">LITTLE SUNBEAM CABINS</span></div>

    <header class="headline">
      <div class="the">THE</div>
      <div class="name">“CLASSIC BARNHOUSE MINI”</div>
      <div class="sub">LUXURY, MOBILE VENDING HOUSE</div>
    </header>

    <div class="thumbs">
      <div class="thumb" role="img" aria-label="Side view of the trailer with open serving window on tandem wheels"></div>
      <div class="thumb" role="img" aria-label="Front view of the trailer showing the entry door"></div>
      <div class="thumb" role="img" aria-label="Rear three-quarter view of the white trailer"></div>
    </div>

    <div class="features-box"></div>
    <h2 class="section-title features-title"><span>BASE UNIT FEATURES</span></h2>
    <ul class="list features-left">
      <li>Trailer features tandem wheels w/ brakes</li>
      <li>Steel frame construction for fire retardation safety and weight reduction.</li>
      <li>100% off grid with solar and lithium battery system allowing the trailer to be used in places not accessible by traditional trailers.</li>
    </ul>
    <div class="divider"></div>
    <ul class="list features-right">
      <li>80 gallon water supply tank</li>
      <li>100 gallon waste water tank</li>
      <li>Cupboards, cabinets &amp; four stainless steel sinks.</li>
      <li>60” Gas shock serving window</li>
    </ul>
    <div class="price-pill"><span class="label">BASE PRICE</span><span class="amount">$45,000</span></div>

    <section class="options-band" role="img" aria-label="Green-tinted photo of the trailer interior behind the options"></section>
    <div class="rule" style="left:178px;width:100px"></div>
    <div class="rule" style="left:540px;width:100px"></div>
    <h2 class="section-title options-title">AVAILABLE OPTIONS</h2>
    <ul class="options-list options-left">
      <li style="margin-bottom:6px">HVAC - Coolwave Mini Split</li>
      <li style="margin-bottom:4px">Cooler / Glass front<br>Commercial refrigerator</li>
      <li>Upper loft storage area</li>
    </ul>
    <div class="tag" style="left:276px;top:829px">$1,800</div>
    <div class="tag sm" style="left:276px;top:864px">$1,600</div>
    <div class="tag sm" style="left:276px;top:899px">$1,200</div>
    <div class="opt-divider"></div>
    <ul class="options-list options-right">
      <li style="margin-bottom:4px">Signage and graphics<span class="note">depend on complexity</span></li>
      <li>Ice machine</li>
      <li>Other custom items<br>available on request</li>
    </ul>
    <div class="tag sm" style="left:640px;top:838px">$2,000-$5,000</div>
    <div class="tag sm" style="left:652px;top:867px">$1,100</div>

    <svg class="usecases-tab" viewBox="0 0 236 40" aria-hidden="true">
      <path d="M0 0 L236 0 L222 28 Q216 40 204 40 L32 40 Q20 40 14 28 Z" fill="#eba714"/>
    </svg>
    <h2 class="usecases-title">USE CASES</h2>
    <ul class="cases cases-left">
      <li><span class="case-name">FOOD</span><span class="case-desc">Lemonade, Coffee, pizza, cookies, doughnuts,<br>barbecue and more!</span></li>
      <li><span class="case-name">RETAIL</span><span class="case-desc">Clothing, watches, jewelry, flowers and more!</span></li>
    </ul>
    <ul class="cases cases-right">
      <li><span class="case-name">CORPORATE</span><span class="case-desc">Product info, demonstration, information,<br>brand awareness.</span></li>
      <li><span class="case-name">FUNDRAISERS</span><span class="case-desc">Girls/boy sports, non profits, etc</span></li>
    </ul>
    <div class="bottom-bar"></div>
  </article>
</div>
</body>
</html>
```